New Church Home Page and Content Page Design

Our church, Cedar Hollow Baptist Church www.chbcfenway.example, needs an update for our online presence. The homepage design should provide the following 4 pieces of information above the fold:
1. Church location - 47 Linden Brook Lane in Chappaqua, NY, USA.
2. Service times and types Sunday school, children's church, etc..
3. A space for some text describing us and our beliefs - a Bible believing independent Baptist church.
4. photos of our members to give visitors an impression of what kind of people attend our church - a friendly group of culturally diverse people who love Jesus.

In addition to the homepage we need a design for internal pages of general content. The content page design should provide a lot of room for content and prominent navigation area. We will use this design to host pages with content such as:
A full description of our beliefs
A photo gallery
An event calendar
Embedded audio and video of past sermons
A member directory
etc.
Updates

Thanks everyone for your submissions. I'll be meeting with our Pastor tomorrow. I am working as fast as I can to review all the designs and come up with a short list for him. A decision should be close behind.

Target Market(s)

Local people looking for a church.

Industry/Entity Type

Church

Requirements
Must have
• 1. Place to show church location - Westchester county, New York State, USA.
2. Place to list service times and types.
3. A space for some text describing us and our beliefs.
4. A place to display photos of our members (see also the nice to have section)
Nice to have
• Would be great if the member photos (#4 in must have section) displayed the images in some innovative way. I rather not have an ordinary carousel of images.

```html
<!DOCTYPE html>
<html lang="en">
<head>
<meta charset="utf-8">
<title>Cedar Hollow Baptist Church</title>
<link href="https://fonts.googleapis.com/css2?family=Open+Sans:wght@400;600&family=PT+Sans:wght@400;700&family=Oswald:wght@500&display=swap" rel="stylesheet">
<style>
:root{
  --navy:#1c3557;
  --navy-dark:#13284a;
  --text:#777;
  --line:#dcdcdc;
  --orange:#f5c063;
  --teal:#5fcac0;
  --green:#7dc275;
  --salmon:#f5836a;
  --footer:#333;
  --white:#fff;
}
*{box-sizing:border-box;margin:0;padding:0}
html,body{width:694px;height:1200px;overflow:hidden;background:var(--white)}
body{position:relative;font-family:"Open Sans",Arial,sans-serif;color:var(--text)}
.abs{position:absolute}

/* header */
.brand{left:50px;top:26px;display:flex;align-items:center;gap:8px}
.brand-mark{width:14px;height:14px;background:var(--navy)}
.brand-name{font-family:"Oswald",sans-serif;font-weight:500;font-size:13px;line-height:16px;color:var(--navy);width:90px}
.address{right:33px;top:21px;font-size:10px;color:var(--navy);display:flex;align-items:center;gap:8px}
.search{right:33px;top:49px;width:150px;height:21px;border:1px solid #ccc;font-size:9px;color:#888;padding:4px 8px;display:flex;justify-content:space-between;align-items:center}

/* hero */
.hero{left:0;top:91px;width:694px;height:277px;background:linear-gradient(160deg,#4d7fb8 0%,#9fc1e0 40%,#eef4f8 55%,#8fb3d6 75%,#5e89b8 100%);border-bottom:3px solid var(--navy)}
.hero-arrow{top:128px;width:36px;height:36px;border-radius:50%;background:rgba(90,90,90,.55);display:flex;align-items:center;justify-content:center}
.hero-caption{left:79px;top:198px;background:rgba(60,60,60,.75);color:var(--white);font-family:"PT Sans",sans-serif;font-size:18px;padding:8px 19px;letter-spacing:.3px}

/* intro */
.h-sec{font-family:"PT Sans",sans-serif;font-size:16px;color:var(--navy);text-transform:uppercase}
.welcome{left:50px;top:397px;width:340px}
.welcome p{margin-top:10px;font-size:8.6px;line-height:16.4px}
.beliefs{left:457px;top:397px;width:186px}
.beliefs .photo{margin:10px 0 0 2px;width:184px;height:76px;background:linear-gradient(180deg,#c7a77e,#7a5236)}
.beliefs p{margin-top:10px;font-size:8.6px;line-height:16.4px;padding-left:2px}

/* section title bars */
.bar-title{left:50px;width:593px;height:18px;display:flex;align-items:center}
.bar-title .rule{flex:1;height:3px;border-top:1px solid var(--line);border-bottom:1px solid var(--line)}
.bar-title .h-sec{padding:0 20px;font-size:14px}
.bar-title .nav{display:flex;gap:3px;margin-left:10px}
.bar-title .dot{width:15px;height:15px;border-radius:50%;background:#ccc;display:flex;align-items:center;justify-content:center}

/* services */
.service{top:645px;width:133px;text-align:center}
.service .photo{height:79px;border:3px solid #ddd}
.service h3{font-family:"PT Sans",sans-serif;font-weight:400;font-size:12px;color:#333;margin:12px 0 6px}
.service .when{background:var(--navy);color:var(--white);font-size:10px;font-family:Arial,sans-serif;height:25px;line-height:25px}

/* members */
.members{left:50px;top:867px;width:593px;height:227px;display:grid;grid-template-columns:repeat(4,1fr);grid-template-rows:repeat(2,1fr);gap:1px;background:#eee}
.tile{color:var(--white);text-align:center;padding-top:16px;position:relative}
.tile h4{font-family:"PT Sans",sans-serif;font-weight:400;font-size:15px;padding-bottom:8px;margin:0 14px 8px;border-bottom:1px solid rgba(255,255,255,.6)}
.tile p{font-size:8.5px;line-height:12px;padding:0 16px}
.tile .more{display:block;font-size:9px;margin-top:11px}
.orange{background:var(--orange)}
.teal{background:var(--teal)}
.green{background:var(--green)}
.salmon{background:var(--salmon)}
.orange::before{content:"";position:absolute;left:-6px;top:50px;border:6px solid transparent;border-left:0;border-right-color:var(--orange)}
.portrait-a{background:linear-gradient(180deg,#f4f5f6,#cfd3d8)}
.portrait-b{background:linear-gradient(180deg,#e9f3f6,#b9d8e2)}
.portrait-c{background:linear-gradient(135deg,#f3e2b8,#9a6a3e)}
.portrait-d{background:linear-gradient(180deg,#f2f2f2,#c9c9cc)}

/* footer */
.footer{left:0;top:1129px;width:694px;height:71px;background:var(--footer);color:#eee;font-size:8.5px}
.footer .links{position:absolute;left:50px;top:18px}
.footer .copy{position:absolute;left:50px;top:40px}
.social{position:absolute;right:51px;top:20px;display:flex;gap:9px}
.social span{width:20px;height:20px;display:block}
</style>
</head>
<body>

<header>
  <div class="abs brand"><span class="brand-mark"></span><span class="brand-name">Cedar Hollow Baptist Church</span></div>
  <div class="abs address">
    <svg width="9" height="13" viewBox="0 0 9 13"><path d="M4.5 0A4.5 4.5 0 0 0 0 4.5C0 8 4.5 13 4.5 13S9 8 9 4.5A4.5 4.5 0 0 0 4.5 0z" fill="#1c3557"/><circle cx="4.5" cy="4.5" r="1.7" fill="#fff"/></svg>
    47 Linden Brook Lane, Chappaqua, NY, USA
  </div>
  <div class="abs search"><span>Search..</span>
    <svg width="9" height="9" viewBox="0 0 9 9"><circle cx="3.7" cy="3.7" r="2.8" fill="none" stroke="#888" stroke-width="1.2"/><line x1="5.8" y1="5.8" x2="8.5" y2="8.5" stroke="#888" stroke-width="1.4"/></svg>
  </div>
</header>

<section class="abs hero" role="img" aria-label="Wooden cross against a bright sky with sun rays and clouds">
  <div class="abs hero-arrow" style="left:51px"><svg width="10" height="14" viewBox="0 0 10 14"><path d="M8 1L2 7l6 6" fill="none" stroke="#fff" stroke-width="1.5"/></svg></div>
  <div class="abs hero-arrow" style="right:51px"><svg width="10" height="14" viewBox="0 0 10 14"><path d="M2 1l6 6-6 6" fill="none" stroke="#fff" stroke-width="1.5"/></svg></div>
  <div class="abs hero-caption">DUS AUTM VEUM IRIRE DOOR DUIS MOLLIS</div>
</section>

<section class="abs welcome">
  <h2 class="h-sec">Welcome to Cedar Hollow Baptist Church</h2>
  <p>Lorem ipsum dolor sit amet, consectetur adipiisicing elit. Suscipit illo voluptas aperiam repudiandae impedit quidem. Lorem ipsum dolor sit amet, cctetur adipisicing elit. Suscipit illo voluptas aperiam repudiandae impeidit quidem. Lorem ipsum dolor sit amet, consectetur adipisicing elit. Suscipit illo voluptas aperiam repudiandae impedit quidem. Lorem ipsum dolor sit amet, consectetur adipisicing elit. Suscipit illo voluptas aperiam repudiandae impedit quidem. Lorem ipsum dolor sit amet, consectetur adipisicing elit. Suscipit illo voluptas aperiam repud. Claritas est etiam processus dynamicus, qui sequitur mutationem consuetudium Duis autem vel eum iriure dolor in hendrerit in vulputate velit esse molestie consequat, vel illum.</p>
</section>

<section class="abs beliefs">
  <h2 class="h-sec">Our Beliefs</h2>
  <div class="photo" role="img" aria-label="Silhouettes of people raising hands before a cross at sunset"></div>
  <p>Our next wave of projects have been acquird during 2010 and 2011 and include a numbeof retail and residential developments.</p>
</section>

<div class="abs bar-title" style="top:602px">
  <span class="rule"></span><h2 class="h-sec">Our Services</h2><span class="rule"></span>
  <span class="nav"><span class="dot"><svg width="5" height="7" viewBox="0 0 5 7"><path d="M4 0.5L1 3.5l3 3" fill="none" stroke="#fff"/></svg></span><span class="dot"><svg width="5" height="7" viewBox="0 0 5 7"><path d="M1 0.5l3 3-3 3" fill="none" stroke="#fff"/></svg></span></span>
</div>

<article class="abs service" style="left:50px"><div class="photo" role="img" aria-label="Congregation gathered around a processional cross" style="background:linear-gradient(135deg,#b8744c,#5c3b2c)"></div><h3>Sunday school</h3><div class="when">27 Apr 2017 | 09:00 am</div></article>
<article class="abs service" style="left:202px"><div class="photo" role="img" aria-label="Hands holding an open Bible in black and white" style="background:linear-gradient(135deg,#d9d9d9,#2d2d2d)"></div><h3>Children's Church</h3><div class="when">27 Apr 2017 | 09:00 am</div></article>
<article class="abs service" style="left:361px"><div class="photo" role="img" aria-label="White chapel under a deep blue sky" style="background:linear-gradient(180deg,#1c3f8c,#6d8fc4 60%,#9aa7b7)"></div><h3>Lorem Ipsum</h3><div class="when">27 Apr 2017 | 09:00 am</div></article>
<article class="abs service" style="left:509px"><div class="photo" role="img" aria-label="Woman praying quietly in soft light" style="background:linear-gradient(135deg,#eee4cf,#9a6a4c)"></div><h3>Non commodo luct</h3><div class="when">27 Apr 2017 | 09:00 am</div></article>

<div class="abs bar-title" style="top:824px">
  <span class="rule"></span><h2 class="h-sec">Our Memebrs</h2><span class="rule"></span>
  <span class="nav"><span class="dot"><svg width="5" height="7" viewBox="0 0 5 7"><path d="M4 0.5L1 3.5l3 3" fill="none" stroke="#fff"/></svg></span><span class="dot"><svg width="5" height="7" viewBox="0 0 5 7"><path d="M1 0.5l3 3-3 3" fill="none" stroke="#fff"/></svg></span></span>
</div>

<section class="abs members">
  <div class="portrait-a" role="img" aria-label="Portrait of a smiling man in a suit"></div>
  <div class="tile orange"><h4>Mr. Alan Reyes</h4><p>Maseleme leifendeuctor wisnes nera iliquam eratutpas rutrem.</p><span class="more">Read More</span></div>
  <div class="portrait-b" role="img" aria-label="Portrait of a smiling woman beside a wall clock"></div>
  <div class="tile teal"><h4>Ms.Nora Hale</h4><p>Maseleme leifendeuctor wisnes nera iliquam eratutpas rutrem.</p><span class="more">Read More</span></div>
  <div class="tile green"><h4>Ms.Ivy Lund</h4><p>Maseleme leifendeuctor wisnes nera iliquam eratutpas rutrem.</p><span class="more">Read More</span></div>
  <div class="portrait-c" role="img" aria-label="Woman in profile praying in warm light"></div>
  <div class="tile salmon"><h4>Mr. Okafor</h4><p>Maseleme leifendeuctor wisnes nera iliquam eratutpas rutrem.</p><span class="more">Read More</span></div>
  <div class="portrait-d" role="img" aria-label="Portrait of a smiling young man in a casual shirt"></div>
</section>

<footer class="abs footer">
  <div class="links">Home | Contact Us | Calendar | Ministries | Service Times | Sermons and Media</div>
  <div class="copy">Copyright © 2013. All Rights Reserved.</div>
  <div class="social"><span style="background:#3b5998"></span><span style="background:#2fa3d8"></span><span style="background:#f26f21"></span><span style="background:#d8262e"></span></div>
</footer>

</body>
</html>
```